Business Card Velostra - Accounting firm

Hi my friend.
I'm coming back to you to see if it would be possible for you to make a modern and minimalist business card design.
In shades of blue like the great logo you offered me.
The ideal is a modern and aesthetic business card.
The goal is to give a professional effect to the first exchanges.
Renewal and innovation in the accounting world !!
I thank you !!
Good evening to you

Target Market(s)

Young, dynamic and sensitive to marketing

Industry/Entity Type

Finance And Accounting

Contact Information for Business Card

Company logo and name. Last name, First name, Phone number, email address, company address, website.

Font styles to use
Sans Serif

Requirements
Must have
• The ideal is a modern and aesthetic business card.

Mentions to include: Company logo and name. Last name, First name, Phone number, email address, company address, website.
Nice to have
• The goal is to give a professional effect to the first exchanges.
Should not have
• Simplistic or childish design

```html
<!DOCTYPE html>
<html lang="en">
<head>
<meta charset="utf-8">
<title>Velostra – Business Card</title>
<link href="https://fonts.googleapis.com/css2?family=Open+Sans:ital,wght@0,400;0,600;0,700;1,400&display=swap" rel="stylesheet">
<style>
  :root {
    --page: #1b1b1d;
    --navy: #1c2966;
    --navy-deep: #18235a;
    --pattern-light: #26408c;
    --teal: #4cc3c0;
    --blue-bright: #2d8fd8;
    --white: #ffffff;
    --text-soft: #e8ecf7;
  }
  * { box-sizing: border-box; margin: 0; padding: 0; }
  html, body { width: 1200px; height: 900px; overflow: hidden; }
  body {
    background: var(--page);
    font-family: "Open Sans", Arial, sans-serif;
    display: flex;
    flex-direction: column;
    align-items: center;
    justify-content: center;
    gap: 46px;
  }
  .card {
    width: 660px;
    height: 377px;
    background: var(--navy);
    position: relative;
    overflow: hidden;
    box-shadow: 0 10px 30px rgba(0,0,0,0.5);
  }
  /* Front */
  .card-front { display: flex; align-items: center; }
  .brand {
    width: 330px;
    padding-left: 52px;
    display: flex;
    flex-direction: column;
  }
  .brand-row { display: flex; align-items: center; gap: 12px; }
  .brand-mark {
    width: 16px; height: 16px;
    background: var(--teal);
  }
  .brand-name {
    font-size: 46px;
    font-weight: 600;
    color: var(--white);
    letter-spacing: -0.5px;
    line-height: 1;
  }
  .brand-tagline {
    margin-top: 8px;
    margin-left: 28px;
    font-size: 10px;
    letter-spacing: 5px;
    color: var(--text-soft);
    text-transform: uppercase;
  }
  .divider {
    width: 1.5px;
    height: 175px;
    background: var(--blue-bright);
    margin-right: 26px;
  }
  .contact { color: var(--white); font-size: 15px; line-height: 1.45; }
  .contact-name {
    color: var(--teal);
    font-weight: 700;
    font-size: 19px;
    text-transform: uppercase;
    letter-spacing: 0.5px;
  }
  .contact-role { font-style: italic; margin-bottom: 8px; }
  .contact-address { margin-bottom: 8px; }
  .contact-line { display: flex; align-items: center; gap: 8px; }
  .contact-line svg { width: 12px; height: 12px; flex: none; }
  /* Back */
  .card-back { display: flex; align-items: flex-end; justify-content: flex-end; }
  .back-pattern {
    position: absolute; inset: 0;
    background: linear-gradient(135deg, var(--navy-deep) 0%, var(--pattern-light) 55%, var(--navy-deep) 100%);
  }
  .back-brand {
    position: relative;
    margin: 0 44px 40px 0;
    display: flex; align-items: center; gap: 10px;
  }
  .back-brand .brand-name { font-size: 30px; }
  .back-brand .brand-mark { width: 12px; height: 12px; }
</style>
</head>
<body>
  <section class="card card-front" aria-label="Business card front">
    <div class="brand">
      <div class="brand-row">
        <span class="brand-mark"></span>
        <span class="brand-name">Velostra</span>
      </div>
      <span class="brand-tagline">Expert-Comptable</span>
    </div>
    <div class="divider"></div>
    <div class="contact">
      <p class="contact-name">Daniel Ferrand</p>
      <p class="contact-role">President</p>
      <p class="contact-address">1870 Harbor Crest Way<br>Bayview CA 90412</p>
      <p class="contact-line">
        <svg viewBox="0 0 12 12" aria-hidden="true"><path d="M2 1 L4.5 1 L5.5 3.5 L4 4.7 C4.8 6.5 5.5 7.2 7.3 8 L8.5 6.5 L11 7.5 L11 10 C6 10.5 1.5 6 2 1Z" fill="var(--teal)"/></svg>
        555-013-4782
      </p>
      <p class="contact-line">
        <svg viewBox="0 0 12 12" aria-hidden="true"><rect x="0.5" y="2.5" width="11" height="7.5" fill="var(--teal)"/><path d="M0.5 2.5 L6 7 L11.5 2.5" stroke="var(--navy)" stroke-width="1" fill="none"/></svg>
        dferrand@velostra.com
      </p>
      <p class="contact-line">
        <svg viewBox="0 0 12 12" aria-hidden="true"><circle cx="6" cy="6" r="5.2" fill="var(--teal)"/><path d="M0.8 6 H11.2 M6 0.8 C3.5 3.5 3.5 8.5 6 11.2 M6 0.8 C8.5 3.5 8.5 8.5 6 11.2" stroke="var(--navy)" stroke-width="0.8" fill="none"/></svg>
        www.velostra.com
      </p>
    </div>
  </section>

  <section class="card card-back" aria-label="Business card back">
    <div class="back-pattern" role="img" aria-label="Repeating embossed pattern of stacked rounded shapes in tones of navy blue"></div>
    <div class="back-brand">
      <span class="brand-mark"></span>
      <span class="brand-name">Velostra</span>
    </div>
  </section>
</body>
</html>
```